New Business Card Design Project for Handyman Business

I would like to purchase a customized version of a design you have previously submitted - https://www.plimvaro.example/work/58302716
I love this design!
I am hoping you can design something similar to this for our Handyman Business.
Attached is our logo and some graphics we have used.
Here is a link to the Google Doc with the content that needs to be included, https://files.trenowick.example/sheet/q/4XRKW-7hLp2DnQv8sTc5ma-ZzoeB3kWu9YyTgp6HJ__RmwNdVcQeLbs4jfnv0ztqxhaK7M41p9ggWHe/view
Target Market(s)
Real Estate Agents, Home Owners and Property Managers
Industry/Entity Type
Construction/ Speciality Trade
Contact Information for Business Card
https://files.trenowick.example/sheet/7QpaRzN_ukoyb4cXTwLHhJe8KnuSbPjCr2QDaLy6nwod/view?mode=shared
Font styles to use
Other font styles liked:
- Ubuntu
Look and feel
Each slider illustrates characteristics of the customer's brand and the style your logo design should communicate.

```html
<!DOCTYPE html>
<html lang="en">
<head>
<meta charset="utf-8">
<title>Brightnook Business Card</title>
<link rel="stylesheet" href="https://fonts.googleapis.com/css2?family=Montserrat:wght@400;600;700&family=Ubuntu:wght@500;700&display=swap">
<style>
  :root {
    --bg: #3a3a3a;
    --card-blue: #0b5f9e;
    --card-blue-light: #1368ab;
    --brand-green: #4cb748;
    --accent-orange: #ec6a2c;
    --white: #ffffff;
    --rule: rgba(255,255,255,0.45);
    --photo-tone: #cfe3ef;
  }
  * { box-sizing: border-box; margin: 0; padding: 0; }
  html, body { width: 1200px; height: 1200px; overflow: hidden; }
  body {
    background: var(--bg);
    display: flex;
    align-items: center;
    justify-content: center;
    gap: 70px;
    font-family: "Montserrat", sans-serif;
    color: var(--white);
  }
  .card {
    width: 420px;
    height: 735px;
    border-radius: 30px;
    background: var(--card-blue);
    border: 4px solid var(--brand-green);
    display: flex;
    flex-direction: column;
    align-items: center;
    text-align: center;
    padding: 90px 36px 50px;
  }
  .card--back { background: var(--card-blue-light); justify-content: flex-end; padding-bottom: 120px; }
  .brand { display: flex; flex-direction: column; align-items: center; gap: 8px; }
  .brand__row { display: flex; align-items: center; gap: 12px; }
  .brand__square { width: 34px; height: 34px; background: var(--brand-green); }
  .brand__name {
    font-family: "Ubuntu", sans-serif;
    font-weight: 700;
    font-size: 50px;
    color: var(--white);
    letter-spacing: 0.5px;
  }
  .brand__tagline {
    font-family: "Ubuntu", sans-serif;
    font-weight: 500;
    font-size: 15px;
    letter-spacing: 4px;
    color: var(--accent-orange);
  }
  .portrait {
    margin-top: 40px;
    width: 170px;
    height: 150px;
    border: 4px solid var(--brand-green);
    background: linear-gradient(160deg, #ffffff 0%, var(--photo-tone) 100%);
  }
  .person__name {
    margin-top: 30px;
    font-weight: 700;
    font-size: 30px;
    letter-spacing: 1px;
  }
  .person__role {
    font-size: 17px;
    color: var(--brand-green);
    letter-spacing: 1px;
    margin-top: 2px;
  }
  .rule { width: 84%; height: 1px; background: var(--rule); margin: 18px 0; }
  .contact { font-size: 21px; line-height: 1.35; }
  .services__headline {
    font-weight: 700;
    font-size: 14px;
    color: var(--brand-green);
    letter-spacing: 0.5px;
  }
  .services__list {
    margin-top: 6px;
    font-weight: 700;
    font-size: 14px;
    display: flex;
    align-items: center;
    gap: 8px;
  }
  .services__dot { width: 7px; height: 7px; background: var(--brand-green); transform: rotate(45deg); }
  .social { display: flex; align-items: center; gap: 10px; margin-top: 40px; }
  .social__line { width: 50px; height: 2px; background: var(--brand-green); }
  .social__icon { width: 40px; height: 40px; border: 2px solid var(--brand-green); border-radius: 50%; }
  .hashtag { margin-top: 16px; font-weight: 700; font-size: 17px; }
</style>
</head>
<body>
  <section class="card card--front">
    <div class="brand">
      <div class="brand__row">
        <span class="brand__square"></span>
        <span class="brand__name">brightnook</span>
      </div>
      <span class="brand__tagline">HOME CARE SPECIALISTS</span>
    </div>
    <div class="portrait" role="img" aria-label="Portrait photo of the owner"></div>
    <h1 class="person__name">OWEN CALDER</h1>
    <p class="person__role">OWNER / HANDYMAN</p>
    <div class="rule"></div>
    <div class="contact">
      <p>(555) 014-2290</p>
      <p>owen@brightnook.example</p>
      <p>brightnook.example</p>
    </div>
    <div class="rule"></div>
    <div class="services">
      <p class="services__headline">COMMERCIAL AND RESIDENTIAL HANDYMAN</p>
      <div class="services__list">
        <span>IMPROVE</span><span class="services__dot"></span>
        <span>REPAIR</span><span class="services__dot"></span>
        <span>REMODEL</span><span class="services__dot"></span>
        <span>MAINTAIN</span>
      </div>
    </div>
  </section>

  <section class="card card--back">
    <div class="brand">
      <div class="brand__row">
        <span class="brand__square"></span>
        <span class="brand__name">brightnook</span>
      </div>
      <span class="brand__tagline">HOME CARE SPECIALISTS</span>
    </div>
    <div class="social">
      <span class="social__line"></span>
      <span class="social__icon"></span>
      <span class="social__icon"></span>
      <span class="social__icon"></span>
      <span class="social__icon"></span>
      <span class="social__line"></span>
    </div>
    <p class="hashtag">#BrightnookHandymanServices</p>
  </section>
</body>
</html>
```